Harbor Tandem Web Design Project

We need a website design for a start up company called "Harbor Tandem". We provide business consultancy services as well as technology-related services (IT). The design should communicate simplicity and elegance. The domain name of the site will be harbortandem.com. The logo of the company is https://files.pinvault.net/u/8147206/7730_2049185_31947_image.jpg
Updates

Target Market(s)

SMB, Corporates, Semi-governments, Governments.

Industry/Entity Type

Business

Requirements
Must have
• - The background of the pages should be white or soft grey, but we are open for suggestions.
- The pages should have nice menu animations.
- The pages should be "portal-style", with multiple placeholders for different sections and multiple tabs.
Nice to have
• The page should auto-fit the screen and scroll vertically as much as needed.
Should not have
• - Flash Animations.
- Generic Photos.

```html
<!DOCTYPE html>
<html lang="en">
<head>
<meta charset="utf-8">
<title>Harbor Tandem</title>
<link href="https://fonts.googleapis.com/css2?family=Open+Sans:wght@400;600&display=swap" rel="stylesheet">
<style>
:root{
  --page:#e8e8e8;
  --header:#ececec;
  --footer:#f4f4f4;
  --card:#f3f3f3;
  --card-line:#dcdcdc;
  --brand:#0d4f9f;
  --brand-dark:#0a3f82;
  --ink:#2b2b2b;
  --body:#5a5a5a;
  --muted:#777;
  --rule:#cfcfcf;
}
*{box-sizing:border-box;margin:0;padding:0}
html,body{width:947px;height:1200px;overflow:hidden}
body{background:var(--page);font-family:"Open Sans",Arial,sans-serif;color:var(--body);position:relative}
.abs{position:absolute}

/* header */
.site-header{position:absolute;left:0;top:0;width:947px;height:170px;background:var(--header)}
.brand{position:absolute;left:103px;top:84px;display:flex;align-items:center;gap:8px}
.brand-dot{width:14px;height:14px;background:var(--brand);border-radius:50%}
.brand-name{font-size:18px;font-weight:600;color:var(--brand);letter-spacing:-.2px}
.search{position:absolute;left:668px;top:44px;width:174px;height:26px;background:#f7f7f7;border:1px solid #e0e0e0}
.search span{position:absolute;left:8px;top:7px;font-size:7px;color:#bbb}
.search svg{position:absolute;right:6px;top:5px}
.main-nav{position:absolute;top:97px;left:0;width:947px;height:20px}
.main-nav a{position:absolute;top:0;height:19px;line-height:19px;font-size:9.5px;color:var(--ink);text-decoration:none}
.main-nav a.active{background:var(--brand);color:#fff;font-weight:600;border-radius:3px;width:63px;text-align:center}

/* hero */
.hero{position:absolute;left:0;top:150px;width:947px;height:387px;overflow:hidden}
.hero-visual{position:absolute;inset:0;background:linear-gradient(90deg,#cfe0ee 0%,#a9c8e2 25%,#7ea7cf 45%,#2b4a86 65%,#1a2c5a 85%,#3a5486 100%)}
.hero-curve{position:absolute;left:0;top:0}
.hero-caption{position:absolute;left:0;top:315px;width:947px;height:72px;background:rgba(60,60,60,.72)}
.hero-caption h1{position:absolute;left:0;width:947px;top:16px;text-align:center;color:#fff;font-weight:400;font-size:20px;letter-spacing:.2px}
.dots{position:absolute;top:45px;left:444px;display:flex;gap:5px}
.dots i{width:11px;height:11px;border-radius:50%;background:#d8d8d8}
.dots i.on{background:#444}

/* services */
.service{position:absolute;top:565px;width:238px;height:153px;background:var(--card);border:1px solid var(--card-line)}
.service-head{height:65px;border-bottom:1px solid var(--card-line);position:relative}
.service-head svg{position:absolute}
.service-title{position:absolute;top:19px;font-size:12.5px;line-height:17px;color:var(--ink);text-transform:uppercase}
.service p{font-size:8.3px;line-height:14.2px;text-align:center;margin:6px 22px 0}
.btn{position:absolute;left:63px;top:132px;width:110px;height:31px;background:var(--brand);color:#fff;font-size:10px;font-weight:600;line-height:31px;text-align:center;border-radius:3px;text-decoration:none}

/* content */
.section-title{position:absolute;top:758px;font-size:12.5px;color:var(--ink);font-weight:400}
.rule{position:absolute;height:1px;background:var(--rule)}
.welcome-photo{position:absolute;left:102px;top:795px;width:237px;height:188px;background:linear-gradient(160deg,#e7eef6 0%,#c7d6e6 45%,#d8b8a4 75%,#eef1f4 100%)}
.copy{position:absolute;top:794px;width:237px;font-size:8.3px;line-height:14.2px;text-align:justify}
.testimonials-title{position:absolute;left:0;width:947px;top:1014px;text-align:center;font-size:12.5px;color:var(--ink)}
.quote{position:absolute;left:120px;width:710px;top:1058px;text-align:center;font-size:10px;line-height:19px;color:#444}
.qmark{position:absolute;font-size:20px;font-weight:600;color:#555;line-height:1}

/* footer */
.site-footer{position:absolute;left:0;top:1130px;width:947px;height:70px;background:var(--footer)}
.footer-nav a{position:absolute;top:16px;font-size:8px;color:#444;text-decoration:none}
.copyright{position:absolute;top:36px;left:0;width:947px;text-align:center;font-size:8px;color:#444}
.social{position:absolute;top:16px;left:735px;display:flex;gap:6px}
.social i{width:24px;height:24px;border-radius:50%}
</style>
</head>
<body>

<header class="site-header">
  <div class="brand"><span class="brand-dot"></span><span class="brand-name">Harbor Tandem</span></div>
  <div class="search"><span>Search</span>
    <svg width="16" height="16" viewBox="0 0 16 16"><circle cx="6" cy="6" r="4.2" fill="none" stroke="#333" stroke-width="1.6"/><line x1="9" y1="9" x2="14" y2="13" stroke="#333" stroke-width="2.2" stroke-linecap="round"/></svg>
  </div>
  <nav class="main-nav">
    <a class="active" href="#" style="left:438px">HOME</a>
    <a href="#" style="left:529px">ABOUT US</a>
    <a href="#" style="left:618px">SERVICES</a>
    <a href="#" style="left:703px">CAREERS</a>
    <a href="#" style="left:785px">CONTACT US</a>
  </nav>
</header>

<section class="hero">
  <div class="hero-visual" role="img" aria-label="Businessman touching a transparent digital interface screen with data icons"></div>
  <svg class="hero-curve" width="947" height="30" viewBox="0 0 947 30"><path d="M0 0 H947 V3 Q473 45 0 3 Z" fill="#ececec"/></svg>
  <div class="hero-caption">
    <h1>IT CONSULTING SERVICES BUSINESS CONSULTANCY &amp; TECHNOLOGY</h1>
    <div class="dots"><i class="on"></i><i></i><i></i><i></i></div>
  </div>
</section>

<article class="service" style="left:103px">
  <div class="service-head">
    <svg style="left:33px;top:17px" width="38" height="34" viewBox="0 0 38 34"><rect x="1" y="1" width="36" height="24" rx="2" fill="#3a3a3a"/><rect x="4" y="4" width="30" height="17" fill="#f3f3f3"/><rect x="16" y="25" width="6" height="5" fill="#3a3a3a"/><rect x="10" y="30" width="18" height="3" fill="#3a3a3a"/></svg>
    <div class="service-title" style="left:89px">IT Consultancy<br>Services</div>
  </div>
  <p>Lorem ipsum dolor sit amet, consectetur adipis-icing elit, sed do eiusmod tempor incididunt ut labore et dolore magna aliqua.</p>
  <a class="btn" href="#">READ MORE</a>
</article>

<article class="service" style="left:355px">
  <div class="service-head">
    <svg style="left:38px;top:7px" width="50" height="54" viewBox="0 0 50 54"><path d="M6 20 L30 44 A17 17 0 0 1 6 20 Z" fill="#3a3a3a"/><line x1="18" y1="32" x2="26" y2="24" stroke="#3a3a3a" stroke-width="2"/><path d="M12 40 L6 54 H22 Z" fill="#3a3a3a"/><path d="M28 14 A10 10 0 0 1 38 24" fill="none" stroke="#3a3a3a" stroke-width="2.5"/><path d="M28 7 A17 17 0 0 1 45 24" fill="none" stroke="#3a3a3a" stroke-width="2.5"/></svg>
    <div class="service-title" style="left:98px">Information<br>Technology</div>
  </div>
  <p>Lorem ipsum dolor sit amet, consectetur adipis-icing elit, sed do eiusmod tempor incididunt ut labore et dolore magna aliqua.</p>
  <a class="btn" href="#">READ MORE</a>
</article>

<article class="service" style="left:607px">
  <div class="service-head">
    <svg style="left:26px;top:19px" width="40" height="36" viewBox="0 0 40 36"><path d="M2 0 V34 H40" fill="none" stroke="#3a3a3a" stroke-width="2.5"/><rect x="6" y="4" width="6" height="28" fill="#3a3a3a"/><rect x="14" y="12" width="6" height="20" fill="#3a3a3a"/><rect x="22" y="20" width="6" height="12" fill="#3a3a3a"/><rect x="30" y="26" width="6" height="6" fill="#3a3a3a"/></svg>
    <div class="service-title" style="left:86px">Business<br>Consultancy</div>
  </div>
  <p>Lorem ipsum dolor sit amet, consectetur adipis-icing elit, sed do eiusmod tempor incididunt ut labore et dolore magna aliqua.</p>
  <a class="btn" href="#">READ MORE</a>
</article>

<h2 class="section-title" style="left:103px">WELCOME TO HARBOR TANDEM</h2>
<h2 class="section-title" style="left:608px">WHY WE CHOOSE US ?</h2>
<div class="rule" style="left:103px;top:783px;width:490px"></div>
<div class="rule" style="left:608px;top:783px;width:237px"></div>

<div class="welcome-photo" role="img" aria-label="Hands typing on a laptop keyboard with floating application icons"></div>
<p class="copy" style="left:355px">But I must explain to you how all this mistaken idea of denouncing pleasure and praising pain was born and I will give you a complete account of the system, and expound the actual teachings of the great explorer of the truth, the master-builder of human happiness. No one rejects, dislikes, or avoids pleasure itself, because it is pleasure, but because those who do not know how to pursue pleasure rationally encounter consequences that are extremely painful. Nor again is there anyone who loves or pursues or desires to obtain pain of itself, because it is pain, but because occasion-ally circumstances occur in which toil and pain can procure him some great pleasure. To take a trivial example, which of us ever undertakes laborious.</p>
<p class="copy" style="left:608px">Lorem ipsum dolor sit amet, consectetur adipisicing elit, sed do eiusmod tempor incididunt ut labore et dolore magna aliqua. Ut enim ad minim veniam, quis nostrud exercitation ullamco laboris nisi ut aliquip ex ea commodo consequat. Duis aute irure dolor in reprehenderit in voluptate velit esse cillum dolore eu fugiat nulla pariatur. Excepteur sint occaecat cupid-atat non proident, sunt in culpa qui officia deserunt mollit anim id est laborum.<br>Lorem ipsum dolor sit amet, consectetur adipisicing elit, sed do eiusmod tempor incididunt ut labore et dolore magna aliqua. Ut enim ad minim veniam, quis nostrud exercitation ullamco laboris nisi ut aliquip ex ea commodo consequat. Duis aute irure dolor in reprehender.</p>

<h2 class="testimonials-title">Testimonials</h2>
<div class="rule" style="left:103px;top:1039px;width:742px"></div>
<span class="qmark" style="left:102px;top:1048px">&ldquo;</span>
<p class="quote">Lorem ipsum dolor sit amet, consectetur adipisicing elit, sed do eiusmod tempor incididunt ut labore et dolore magna aliqua. Ut enim ad minim veniam, quis nostrud exercitation ullamco laboris nisi ut aliquip ex ea commodo consequat.</p>
<span class="qmark" style="left:658px;top:1074px">&rdquo;</span>

<footer class="site-footer">
  <nav class="footer-nav">
    <a href="#" style="left:320px">Home</a>
    <a href="#" style="left:380px">About us</a>
    <a href="#" style="left:450px">Services</a>
    <a href="#" style="left:518px">Careers</a>
    <a href="#" style="left:584px">Contact Us</a>
  </nav>
  <p class="copyright">Copyright © 2009 - 2013 Harbor Tandem, All rights reserved. Privacy Policy | T's &amp; C's</p>
  <div class="social">
    <i style="background:#8cc6e6"></i><i style="background:#f2b544"></i><i style="background:#c8242a"></i><i style="background:#3d5a98"></i>
  </div>
</footer>

</body>
</html>
```